Grey year meltdown

UPDATED BRIEF:
I'm just updating the brief to enable any new submissions to come up with their own ideas. I have tried to offer my ideas below, but I am too close to the project therefor any new submissions are probably best using your talent. The main thing is it stands out and someone would want to buy it against the competition. All submissions have been excellent, so to be fair I will put the winning vote to family and friends. I am too close and biased to make the final choice.
This book is part memoire/ part biography/ part diary/ part self help.
My world is falling apart. I use the analogy of being lost at see. This book is my ships log. It could be a torn out PAGE of the log, a POSTER, or A MESSAGE a bottle.
It needs to be clear in the title, so GREY YEAR MELTDOWN needs to stand out. YOLO could be a wax seal, like a stamp. 'You're facing a' and 'You're losing the plot' are less important. The title is: YOLO You're facing a GREY YEAR MELTDOWN You're losing the plot.
Other subliminal random words are: family, paranoia, sex addiction, depression, marriage, divorce.
The other idea is flame red. Needs to be subtle to show my life is going up in flames. The diary page/poster/note should be singed or worn.
Ideally text font should be bespoke. Whether some or all are slightly wonky to show that my life is falling apart.
Octopus bottom left with tentacles spread over spine is a firm favourite
Text on spine needs to be large to stand out. Open to suggestions but nothing over simple.Good luck

Target Market(s)

30-60 years

Colors

Requirements
Must have
• Book size. I'm assuming: 21.5cm x 13.5cm x 2.5cm. I will need ebook version and paperback version. ISBN details will follow later

```html
<!DOCTYPE html>
<html lang="en">
<head>
<meta charset="utf-8">
<title>Grey Year Meltdown – Book Cover</title>
<link href="https://fonts.googleapis.com/css2?family=Anton&family=EB+Garamond:wght@400&display=swap" rel="stylesheet">
<style>
  :root {
    --red-bright: #ee2a34;
    --red-mid: #e0232c;
    --red-deep: #9e1219;
    --spine-red: #e8262f;
    --sign-red: #e11b22;
    --ink: #0d0d0d;
    --paper-light: #fbf9ee;
    --paper-warm: #efe9b8;
    --paper-cool: #cfe1dc;
    --white: #ffffff;
  }
  * { box-sizing: border-box; margin: 0; padding: 0; }
  html, body { width: 1200px; height: 830px; overflow: hidden; background: var(--red-deep); }
  .cover { position: relative; width: 1200px; height: 830px; overflow: hidden; }
  .back-cover {
    position: absolute; left: 0; top: 0; width: 554px; height: 830px;
    background: radial-gradient(ellipse 70% 60% at 50% 48%, var(--red-bright) 0%, var(--red-mid) 55%, var(--red-deep) 100%);
  }
  .spine {
    position: absolute; left: 554px; top: 0; width: 92px; height: 830px;
    background: var(--spine-red);
  }
  .front-cover {
    position: absolute; left: 646px; top: 0; width: 554px; height: 830px;
    background: radial-gradient(ellipse 70% 60% at 50% 50%, var(--red-bright) 0%, var(--red-mid) 55%, var(--red-deep) 100%);
  }
  .warning-sign { position: absolute; display: block; }
  .back-cover .warning-sign { left: 222px; top: 36px; width: 112px; height: 96px; }
  .blurb {
    position: absolute; left: 44px; width: 466px;
    font-family: "EB Garamond", Georgia, serif;
    font-size: 20.4px; line-height: 21.6px;
    color: var(--white); text-align: justify;
  }
  .blurb-hook { top: 150px; }
  .blurb-about { top: 408px; }
  .isbn-box {
    position: absolute; left: 357px; top: 692px; width: 149px; height: 93px;
    background: var(--white);
  }
  .spine-title { position: absolute; left: 0; top: 0; width: 92px; height: 830px; }
  .tagline { position: absolute; left: 54px; top: 28px; width: 450px; height: 42px; }
  .poster {
    position: absolute; left: 52px; top: 82px; width: 449px; height: 648px;
    background:
      radial-gradient(ellipse 60% 50% at 50% 45%, var(--paper-light) 0%, var(--paper-light) 40%, transparent 80%),
      linear-gradient(160deg, var(--paper-warm) 0%, var(--paper-light) 45%, var(--paper-cool) 100%);
  }
  .poster-title { position: absolute; left: 0; top: 0; width: 449px; height: 648px; }
  .author { position: absolute; left: 54px; top: 758px; width: 450px; height: 46px; }
</style>
</head>
<body>
<main class="cover">

  <section class="back-cover">
    <svg class="warning-sign" viewBox="0 0 112 96" aria-hidden="true">
      <polygon points="56,8 104,88 8,88" fill="var(--white)" stroke="var(--sign-red)" stroke-width="12" stroke-linejoin="round"/>
      <path d="M52 30 h8 l-1.5 34 h-5 z" fill="var(--ink)"/>
      <circle cx="56" cy="74" r="5" fill="var(--ink)"/>
    </svg>
    <p class="blurb blurb-hook">So you’ve found your career, got married, bought your home. Life is great, you are happy and everything just seems to fit into place.<br>Then all of a sudden your perfect Utopia starts to fall apart. The life that was once full of promise, hope, and ambition, is now starting to fall apart. You’ve reached the summit and the panoramic view is not what you expected! The storm approaches and you panic. Worry, fear, and distress fill your mind. Congratulations you have reached the Nirvana of a GYM!</p>
    <p class="blurb blurb-about">This book is an honest reflection of life according to a dreamer. Somebody who’s lost his way. A person who has it all, yet, has nothing. Someone who has lost his place in society, has so much to give, yet feels so empty and hopeless inside. A story of living life with depression. The highs and lows of a family man just trying to make it in life. The ultimate guide to a fragile mind in Grey year meltdown fighting: Sex addiction, Periods, the menopause,<br>Marriage conflict, Parenting, finance, Divorce, and Affairs</p>
    <div class="isbn-box" aria-hidden="true"></div>
  </section>

  <section class="spine">
    <svg class="spine-title" viewBox="0 0 92 830" aria-label="YOLO! Grey Year Meltdown – Losing the Plot">
      <text transform="translate(24 40) rotate(90)" font-family="Anton, sans-serif" font-size="50" fill="var(--white)" textLength="420" lengthAdjust="spacingAndGlyphs">YOLO! GREY YEAR MELTDOWN</text>
      <text transform="translate(34 504) rotate(90)" font-family="Anton, sans-serif" font-size="30" fill="var(--white)" textLength="236" lengthAdjust="spacing">LOSING THE PLOT</text>
    </svg>
  </section>

  <section class="front-cover">
    <svg class="tagline" viewBox="0 0 450 42" aria-label="The Number One Homedad">
      <text x="0" y="38" font-family="Anton, sans-serif" font-size="42" fill="var(--white)" textLength="450" lengthAdjust="spacingAndGlyphs">THE NUMBER ONE HOMEDAD</text>
    </svg>

    <div class="poster" role="img" aria-label="Worn, weathered paper poster texture">
      <svg class="poster-title" viewBox="0 0 449 648" aria-label="YOLO You're facing a Grey Year Meltdown You're losing the plot">
        <text x="36" y="114" font-family="Anton, sans-serif" font-size="44" fill="var(--sign-red)" textLength="108" lengthAdjust="spacingAndGlyphs">YOLO</text>
        <text x="166" y="114" font-family="Anton, sans-serif" font-size="38" fill="var(--ink)" textLength="250" lengthAdjust="spacingAndGlyphs">YOU'RE FACING A</text>
        <text x="28" y="232" font-family="Anton, sans-serif" font-size="124" fill="var(--ink)" textLength="396" lengthAdjust="spacingAndGlyphs">GREY YEAR</text>
        <text x="28" y="370" font-family="Anton, sans-serif" font-size="142" fill="var(--ink)" textLength="400" lengthAdjust="spacingAndGlyphs">MELTDOWN</text>
        <text x="30" y="430" font-family="Anton, sans-serif" font-size="44" fill="var(--ink)" textLength="396" lengthAdjust="spacingAndGlyphs">YOU'RE LOSING THE PLOT</text>
        <g class="warning-sign" transform="translate(122 452)">
          <polygon points="100,14 188,166 12,166" fill="var(--white)" stroke="var(--sign-red)" stroke-width="20" stroke-linejoin="round"/>
          <path d="M92 60 h16 l-3 62 h-10 z" fill="var(--ink)"/>
          <circle cx="100" cy="141" r="10" fill="var(--ink)"/>
        </g>
      </svg>
    </div>

    <svg class="author" viewBox="0 0 450 46" aria-label="Rowan Keel">
      <text x="0" y="44" font-family="Anton, sans-serif" font-size="46" fill="var(--white)" textLength="450" lengthAdjust="spacing">R O W A N &#160; K E E L</text>
    </svg>
  </section>

</main>
</body>
</html>
```